Rory Vandermeer | Inbound Marketing

Need a logo for a company that fills the need of creating a consistent stream of warm sales leads and revenue (via building of a sales funnel) to companies who either do not have sales teams or use outmoded outbound sales strategy to address the company bottom line. This includes Inbound marketing, SEO, content marketing strategy

Target Market(s)

Small to Medium Size Businesses, who are willing to spend thousands or tens of thousands of dollars on avertising.

Industry/Entity Type

It Company

Contact Information for Business Card

Leadwell Inbound | PPC | SEO | Local Social & SEO
512.604.7193
roryvandermeer@quillmail.net

Logo Text

Look Inward to Gain Outward

Font styles to use
Sans Serif

Requirements
Nice to have
• I am partial to funnels in natural phenomena (tornados, whirlpools, hurricanes, black holes, spiral galaxies) but this is not a deal breaker. In fact, I don't want to intimidate anybody and seeing photos and artist representation are somewhat unsettling to me as to their vastness and darkness

```html
<!DOCTYPE html>
<html lang="en">
<head>
<meta charset="utf-8">
<title>Leadwell Inbound – Business Card</title>
<link rel="stylesheet" href="https://fonts.googleapis.com/css2?family=Oswald:wght@600&family=Archivo+Black&family=Mulish:wght@400;700&display=swap">
<style>
  :root {
    --backdrop: #eceded;
    --card-dark: #000000;
    --card-light: #ffffff;
    --wordmark-light: #d4d4d4;
    --wordmark-dark: #111111;
    --accent-blue: #2f86d6;
    --text-white: #ffffff;
    --text-main: #333333;
    --icon-blue: #2a55a8;
    --card-shadow: rgba(0, 0, 0, 0.22);
  }
  html, body {
    margin: 0;
    padding: 0;
    width: 1039px;
    height: 1200px;
    overflow: hidden;
    background: var(--backdrop);
  }
  .canvas {
    position: relative;
    width: 1039px;
    height: 1200px;
  }
  .card {
    position: absolute;
    width: 808px;
    height: 468px;
    box-shadow: 0 4px 18px var(--card-shadow);
  }
  .card--front {
    left: 118px;
    top: 105px;
    background: var(--card-dark);
  }
  .card--back {
    left: 124px;
    top: 645px;
    background: var(--card-light);
  }
  .wordmark {
    position: absolute;
    left: 0;
    right: 0;
    display: flex;
    align-items: center;
    justify-content: center;
    gap: 18px;
    font-family: "Oswald", "Arial Narrow", sans-serif;
    font-weight: 600;
    text-transform: uppercase;
    white-space: nowrap;
    line-height: 1;
  }
  .wordmark__dot {
    border-radius: 50%;
    background: var(--accent-blue);
    flex: none;
  }
  .card--front .wordmark {
    top: 130px;
    font-size: 76px;
    letter-spacing: 1px;
    color: var(--wordmark-light);
  }
  .card--front .wordmark__dot {
    width: 40px;
    height: 40px;
  }
  .website {
    position: absolute;
    left: 0;
    right: 0;
    top: 322px;
    text-align: center;
    font-family: "Archivo Black", "Arial Black", sans-serif;
    font-size: 25px;
    letter-spacing: 7px;
    color: var(--text-white);
    text-transform: uppercase;
  }
  .card--back .wordmark {
    top: 100px;
    font-size: 44px;
    color: var(--wordmark-dark);
    gap: 12px;
  }
  .card--back .wordmark__dot {
    width: 24px;
    height: 24px;
  }
  .person {
    position: absolute;
    left: 0;
    right: 0;
    top: 208px;
    text-align: center;
    font-family: "Mulish", "Century Gothic", sans-serif;
    color: var(--text-main);
  }
  .person__name {
    margin: 0;
    font-size: 26px;
    font-weight: 700;
    text-transform: uppercase;
    letter-spacing: 0.5px;
  }
  .person__services {
    margin: 4px 0 0;
    font-size: 27px;
    font-weight: 400;
  }
  .contact {
    position: absolute;
    left: 205px;
    top: 338px;
    margin: 0;
    padding: 0;
    list-style: none;
    font-family: "Mulish", "Century Gothic", sans-serif;
    font-size: 27px;
    color: var(--text-main);
  }
  .contact__item {
    display: flex;
    align-items: center;
    gap: 12px;
    height: 36px;
  }
  .contact__icon {
    width: 28px;
    height: 28px;
    flex: none;
  }
</style>
</head>
<body>
<main class="canvas">
  <section class="card card--front" aria-label="Card front">
    <div class="wordmark">
      <span>Leadwell</span>
      <span class="wordmark__dot" aria-hidden="true"></span>
      <span>Inbound</span>
    </div>
    <p class="website">www.leadwellinbound.com</p>
  </section>

  <section class="card card--back" aria-label="Card back">
    <div class="wordmark">
      <span>Leadwell</span>
      <span class="wordmark__dot" aria-hidden="true"></span>
      <span>Inbound</span>
    </div>
    <div class="person">
      <p class="person__name">Name Surname</p>
      <p class="person__services">PPC | SEO | Local Social &amp; SEO</p>
    </div>
    <ul class="contact">
      <li class="contact__item">
        <svg class="contact__icon" viewBox="0 0 28 28" aria-hidden="true">
          <rect x="7" y="2" width="14" height="24" rx="2.5" fill="none" stroke="var(--icon-blue)" stroke-width="2"/>
          <line x1="7" y1="20" x2="21" y2="20" stroke="var(--icon-blue)" stroke-width="1.6"/>
          <circle cx="14" cy="23" r="1.2" fill="var(--icon-blue)"/>
        </svg>
        <span>512.604.7193</span>
      </li>
      <li class="contact__item">
        <svg class="contact__icon" viewBox="0 0 28 28" aria-hidden="true">
          <rect x="2" y="7" width="24" height="15" rx="1.5" fill="none" stroke="var(--icon-blue)" stroke-width="2"/>
          <polyline points="3,8 14,16 25,8" fill="none" stroke="var(--icon-blue)" stroke-width="2"/>
        </svg>
        <span>roryvandermeer@quillmail.net</span>
      </li>
    </ul>
  </section>
</main>
</body>
</html>
```